Etiketten für Imkerei
Zielgruppe
Wir sind eine Imkerei in München. Die Zielgrppe sind Menschen, die lokale Produkte wertschätzen, beim Produzenten gern direkt und auf Märkten einkaufen.
Hallo,
wir benötigen ein universelles Design für Honiggläser-Etiketten, das für verschiedene Sorten verwendet werden kann. Das vorhanden Logo soll im Design aufgenommen werden. Im Logo reicht der Name: Imkerei-Brunntal.

```html
<!DOCTYPE html>
<html lang="de">
<head>
<meta charset="utf-8">
<title>Honig-Etiketten – Imkerei-Brunntal</title>
<link href="https://fonts.googleapis.com/css2?family=Fira+Sans+Condensed:wght@800&family=Open+Sans:wght@400;600;700&display=swap" rel="stylesheet">
<style>
  :root {
    --canvas-bg: #ffffff;
    --panel-brown: #8a5134;
    --panel-line: #9d5f3c;
    --gold: #d9a12c;
    --gold-dark: #c48a1c;
    --white: #ffffff;
    --band-spring: #f9b987;
    --band-acacia: #c6e09e;
    --band-summer: #f5b1ad;
    --band-forest: #88b998;
    --band-comb: #fdd08d;
  }
  * { margin: 0; padding: 0; box-sizing: border-box; }
  html, body { width: 848px; height: 1200px; overflow: hidden; background: var(--canvas-bg); }
  .sheet { position: relative; width: 848px; height: 1200px; }

  .label-slot { position: absolute; }
  .label-slot--hero { left: 174px; top: 300px; width: 500px; height: 380px; }
  .label-slot--small { top: 918px; width: 200px; height: 152px; }

  .label {
    position: absolute; left: 0; top: 0;
    width: 500px; height: 380px;
    transform-origin: top left;
  }
  .label-slot--small .label { transform: scale(0.4); }

  .side-band { position: absolute; top: 70px; width: 110px; height: 310px; background: var(--band); }
  .side-band--left { left: 0; }
  .side-band--right { right: 0; }

  .center-panel {
    position: absolute; left: 110px; top: 70px; width: 280px; height: 310px;
    background: var(--panel-brown);
    overflow: hidden;
  }
  .center-panel::before {
    content: ""; position: absolute; left: 20px; top: 100px; width: 240px; height: 140px;
    border: 10px solid var(--panel-line); border-radius: 4px; opacity: .6;
  }

  .hex-badge { position: absolute; left: 165px; top: 0; width: 170px; height: 160px; }

  .variety {
    position: absolute; left: 110px; top: 176px; width: 280px;
    text-align: center; color: var(--white); white-space: nowrap;
    font-family: "Open Sans", sans-serif; font-weight: 400; font-size: 23px; letter-spacing: .5px;
  }
  .product {
    position: absolute; left: 110px; top: 204px; width: 260px;
    text-align: center; color: var(--white);
    font-family: "Fira Sans Condensed", sans-serif; font-weight: 800; font-size: 66px; line-height: 1;
  }
  .bee-art {
    position: absolute; left: 328px; top: 232px; width: 58px; height: 50px;
    border-radius: 50%;
    background: radial-gradient(ellipse at center, #e3a62b 0%, #6a4426 50%, rgba(138,81,52,0) 70%);
  }

  .brand {
    position: absolute; left: 150px; top: 296px; width: 230px; height: 36px;
    display: flex; align-items: center; gap: 8px; white-space: nowrap;
    font-family: "Open Sans", sans-serif; font-weight: 600; font-size: 19px; color: var(--white);
  }
  .brand-dot { width: 30px; height: 30px; border-radius: 50%; background: var(--white); flex: none; }

  .quality-strip {
    position: absolute; left: 110px; top: 346px; width: 280px; height: 34px;
    background: var(--gold);
    display: flex; align-items: center; justify-content: space-between; padding: 0 8px;
    font-family: "Open Sans", sans-serif; color: var(--white); white-space: nowrap;
  }
  .quality-stars { font-size: 22px; font-weight: 700; letter-spacing: 2px; line-height: 1; }
  .quality-text { font-size: 13px; font-weight: 700; }
</style>
</head>
<body>
<main class="sheet">

  <!-- Frühlingsblüten -->
  <div class="label-slot label-slot--hero">
    <article class="label" style="--band: var(--band-spring)">
      <div class="side-band side-band--left"></div>
      <div class="side-band side-band--right"></div>
      <div class="center-panel"></div>
      <svg class="hex-badge" viewBox="0 0 170 160">
        <defs><linearGradient id="spring" x1="0" x2="1"><stop offset="0" stop-color="#8cc63f"/><stop offset=".5" stop-color="#f2a74a"/><stop offset="1" stop-color="#c9a89a"/></linearGradient></defs>
        <polygon points="45,8 125,8 162,72 125,136 45,136 8,72" fill="#fff" stroke="var(--gold)" stroke-width="7"/>
        <path d="M148 100 q6 14 0 26 a6 6 0 0 1 -10 -4 q2 -12 10 -22z" fill="var(--gold-dark)"/>
        <circle cx="85" cy="72" r="40" fill="url(#spring)" role="img" aria-label="Bunte Blütenblätter als Sortensymbol"/>
      </svg>
      <div class="variety">FRÜHLINGSBLÜTEN</div>
      <div class="product">Honig</div>
      <div class="bee-art" role="img" aria-label="Illustration einer Honigbiene"></div>
      <div class="brand"><span class="brand-dot"></span>Imkerei-Brunntal</div>
      <div class="quality-strip"><span class="quality-stars">✱✱✱</span><span class="quality-text">Bayrische Qualität</span><span class="quality-stars">✱✱✱</span></div>
    </article>
  </div>

  <!-- Blüten / Akazien -->
  <div class="label-slot label-slot--small" style="left:15px">
    <article class="label" style="--band: var(--band-acacia)">
      <div class="side-band side-band--left"></div>
      <div class="side-band side-band--right"></div>
      <div class="center-panel"></div>
      <svg class="hex-badge" viewBox="0 0 170 160">
        <polygon points="45,8 125,8 162,72 125,136 45,136 8,72" fill="#fff" stroke="var(--gold)" stroke-width="7"/>
        <path d="M148 100 q6 14 0 26 a6 6 0 0 1 -10 -4 q2 -12 10 -22z" fill="var(--gold-dark)"/>
        <circle cx="85" cy="72" r="38" fill="#7cc242" role="img" aria-label="Grünes Blattsymbol"/>
      </svg>
      <div class="variety">BLÜTEN- /AKAZIEN-</div>
      <div class="product">Honig</div>
      <div class="bee-art" role="img" aria-label="Illustration einer Honigbiene"></div>
      <div class="brand"><span class="brand-dot"></span>Imkerei-Brunntal</div>
      <div class="quality-strip"><span class="quality-stars">✱✱✱</span><span class="quality-text">Bayrische Qualität</span><span class="quality-stars">✱✱✱</span></div>
    </article>
  </div>

  <!-- Sommerblüten -->
  <div class="label-slot label-slot--small" style="left:224px">
    <article class="label" style="--band: var(--band-summer)">
      <div class="side-band side-band--left"></div>
      <div class="side-band side-band--right"></div>
      <div class="center-panel"></div>
      <svg class="hex-badge" viewBox="0 0 170 160">
        <polygon points="45,8 125,8 162,72 125,136 45,136 8,72" fill="#fff" stroke="var(--gold)" stroke-width="7"/>
        <path d="M148 100 q6 14 0 26 a6 6 0 0 1 -10 -4 q2 -12 10 -22z" fill="var(--gold-dark)"/>
        <circle cx="85" cy="72" r="38" fill="#e8407a" role="img" aria-label="Pinke Blüte als Sortensymbol"/>
      </svg>
      <div class="variety">SOMMERBLÜTEN</div>
      <div class="product">Honig</div>
      <div class="bee-art" role="img" aria-label="Illustration einer Honigbiene"></div>
      <div class="brand"><span class="brand-dot"></span>Imkerei-Brunntal</div>
      <div class="quality-strip"><span class="quality-stars">✱✱✱</span><span class="quality-text">Bayrische Qualität</span><span class="quality-stars">✱✱✱</span></div>
    </article>
  </div>

  <!-- Wald und Blüten -->
  <div class="label-slot label-slot--small" style="left:433px">
    <article class="label" style="--band: var(--band-forest)">
      <div class="side-band side-band--left"></div>
      <div class="side-band side-band--right"></div>
      <div class="center-panel"></div>
      <svg class="hex-badge" viewBox="0 0 170 160">
        <polygon points="45,8 125,8 162,72 125,136 45,136 8,72" fill="#fff" stroke="var(--gold)" stroke-width="7"/>
        <path d="M148 100 q6 14 0 26 a6 6 0 0 1 -10 -4 q2 -12 10 -22z" fill="var(--gold-dark)"/>
        <circle cx="85" cy="72" r="38" fill="#1d7a3c" role="img" aria-label="Tannenbaum als Sortensymbol"/>
      </svg>
      <div class="variety">WALD- UND BLÜTEN-</div>
      <div class="product">Honig</div>
      <div class="bee-art" role="img" aria-label="Illustration einer Honigbiene"></div>
      <div class="brand"><span class="brand-dot"></span>Imkerei-Brunntal</div>
      <div class="quality-strip"><span class="quality-stars">✱✱✱</span><span class="quality-text">Bayrische Qualität</span><span class="quality-stars">✱✱✱</span></div>
    </article>
  </div>

  <!-- Waben -->
  <div class="label-slot label-slot--small" style="left:642px">
    <article class="label" style="--band: var(--band-comb)">
      <div class="side-band side-band--left"></div>
      <div class="side-band side-band--right"></div>
      <div class="center-panel"></div>
      <svg class="hex-badge" viewBox="0 0 170 160">
        <polygon points="45,8 125,8 162,72 125,136 45,136 8,72" fill="#fff" stroke="var(--gold)" stroke-width="7"/>
        <path d="M148 100 q6 14 0 26 a6 6 0 0 1 -10 -4 q2 -12 10 -22z" fill="var(--gold-dark)"/>
        <polygon points="68,48 102,48 119,72 102,96 68,96 51,72" fill="#d6b000"/>
      </svg>
      <div class="variety">WABEN-</div>
      <div class="product">Honig</div>
      <div class="bee-art" role="img" aria-label="Illustration einer Honigbiene"></div>
      <div class="brand"><span class="brand-dot"></span>Imkerei-Brunntal</div>
      <div class="quality-strip"><span class="quality-stars">✱✱✱</span><span class="quality-text">Bayrische Qualität</span><span class="quality-stars">✱✱✱</span></div>
    </article>
  </div>

</main>
</body>
</html>
```